WWW.VELTRONA.IT BUSINNES CARD

WE NEED A BUSINESS CARD . I HAVE A COMPANY IN ITALY NR 1 IN HAIR MEDICAL CARE AN HAIR REPLECEMENT . IN CARD I NEED WRITE WEB ADDRESS, MAIL , ADDRESS, TELEPHONE NUMBER , AND NAME
IN THE BACK SIDE I NEED MY DOCTOR LOGO .
MY WEB SITE IS WWW.VELTRONA.IT
Updates

Target Market(s)

CONSUMER B2C

Industry/Entity Type

Hair And Beauty

Contact Information for Business Card

I WANT A MEDICAL BUSINESS CARD.

Font styles to use
Other font styles liked:
• VERDANA

Colors
33a6d7
3176b5
85abd2
aedbee
eaf1f7
ffffff

Requirements
Must have
• I NEED MY LOGO AND LOGO OF DR VELTRONA

```html
<!DOCTYPE html>
<html lang="it">
<head>
<meta charset="utf-8">
<title>Veltrona – Biglietto da visita</title>
<link rel="stylesheet" href="https://fonts.googleapis.com/css2?family=Jost:wght@400;700&family=Arimo:wght@400&display=swap">
<style>
  :root {
    --navy: #045393;
    --sky: #1cb0e6;
    --paper: #ffffff;
    --canvas: #fdfdfd;
    --hair-brown: #7a4a2a;
    --skin-peach: #f2b48c;
  }
  html, body {
    margin: 0;
    padding: 0;
    width: 1200px;
    height: 1200px;
    overflow: hidden;
    background: var(--canvas);
  }
  .stage {
    position: relative;
    width: 1200px;
    height: 1200px;
  }
  .card {
    position: absolute;
    left: 360px;
    width: 480px;
    height: 310px;
    box-sizing: border-box;
    border: 10px solid var(--navy);
    background: var(--paper);
  }
  .card--front { top: 248px; }
  .card--back  { top: 640px; }
  .card__rule {
    position: absolute;
    left: 9px;
    top: 11px;
    right: 9px;
    bottom: 9px;
    border: 2px solid var(--sky);
  }
  .card__art {
    position: absolute;
    left: -10px;
    top: -10px;
    width: 480px;
    height: 310px;
  }
  .brand-name {
    position: absolute;
    margin: 0;
    font-family: "Jost", sans-serif;
    font-weight: 700;
    color: var(--navy);
    letter-spacing: 0.02em;
    line-height: 1;
    white-space: nowrap;
  }
  .brand-tagline {
    position: absolute;
    margin: 0;
    font-family: "Jost", sans-serif;
    font-weight: 400;
    color: var(--navy);
    letter-spacing: 0.04em;
    white-space: nowrap;
    line-height: 1;
  }
  .card--front .brand-name,
  .card--front .brand-tagline {
    left: 0;
    right: 0;
    text-align: center;
  }
  .card--front .brand-name { top: 100px; font-size: 50px; }
  .card--front .brand-tagline { top: 164px; font-size: 15px; }
  .card--back .brand-name { left: 39px; top: 44px; font-size: 26px; }
  .card--back .brand-tagline { left: 39px; top: 75px; font-size: 7.6px; }
  .mascot {
    position: absolute;
    left: 22px;
    top: 114px;
    width: 80px;
    height: 148px;
    border-radius: 40px 40px 40px 40px / 60px 60px 20px 20px;
    background: linear-gradient(180deg, var(--hair-brown) 0%, #9a6a48 60%, var(--skin-peach) 100%);
  }
  .contact {
    position: absolute;
    left: 253px;
    top: 172px;
    margin: 0;
    padding: 0;
    list-style: none;
    font-family: "Arimo", sans-serif;
    font-size: 13px;
    color: var(--paper);
  }
  .contact li { height: 30.5px; }
</style>
</head>
<body>
<div class="stage">

  <section class="card card--front">
    <div class="card__rule"></div>
    <h1 class="brand-name">VELTRONA</h1>
    <p class="brand-tagline">CURA E REINTEGRAZIONE DEI CAPELLI</p>
  </section>

  <section class="card card--back">
    <div class="card__rule"></div>
    <svg class="card__art" viewBox="0 0 480 310" aria-hidden="true">
      <path d="M218 291 C206 150 290 40 432 37 L461 37 L461 291 Z" fill="var(--sky)"/>
      <path d="M236 291 C228 155 305 45 430 38 L461 38 L461 291 Z" fill="var(--navy)"/>
    </svg>
    <h2 class="brand-name">VELTRONA</h2>
    <p class="brand-tagline">CURA E REINTEGRAZIONE DEI CAPELLI</p>
    <div class="mascot" role="img" aria-label="Mascotte del dottore: un capello castano illustrato con camice bianco su base arancio chiaro"></div>
    <ul class="contact">
      <li>Add</li>
      <li>Web Add</li>
      <li>Mail Add</li>
    </ul>
  </section>

</div>
</body>
</html>
```